New menu rebranding for Asian fusion

I have my current menu attached, but I want to change it and make it more attractive. The restaurant is an Asian Fusion. Food from Thailand, China, Japan, Indonesia, Malaysia, Cambodia. We cater to mid to high end consumers with an educated and sophisticated pallet. Maybe try a modern twist, or an authentic variation, maybe a mix. Please don't play with the logo too much, but feel free to play with the pattern. I also want to have as many pictures of dishes visible as possible. Additionally, keep in mind that the menu will be in two languages, so please design accordingly. Feel free to play around with the format of the menu and the logo too if you get carried away. Keep it in mind that this is also a take out menu too. Please check out the Instagram account lotus_crate As well as facebook etc. Let me know if you need any additional files. Thx and appreciated.
Updates

I have made an update to the Menu. It's not the original file. It's smaller now. Please see the attached PDF file. Best regards, Added Monday, February 02, 2015

Target Market(s)

Mid to high end

Industry/Entity Type

Restaurant

Number of Pages Required

3 page

Requirements
Must have
• dual language friendly. At least make space for it.
• Must keep logo.
Nice to have
• Would be nice to stick to same theme, not too much change to branding.

```html
<!DOCTYPE html>
<html lang="en">
<head>
<meta charset="utf-8">
<title>Appetizers Menu</title>
<link href="https://fonts.googleapis.com/css2?family=Oswald:wght@300;400;500&family=Cairo:wght@300;400&display=swap" rel="stylesheet">
<style>
  :root {
    --paper: #e2deda;
    --stripe: #f1efed;
    --ink: #1f1c1a;
    --muted: #8f8b88;
    --frame: #ffffff;
    --label: #231f1d;
  }
  html, body { margin: 0; padding: 0; overflow: hidden; }
  body { width: 1200px; height: 849px; background: var(--paper); }
  .menu-page {
    position: relative; width: 1200px; height: 849px; overflow: hidden;
    background: var(--paper);
    font-family: "Oswald", "Arial Narrow", sans-serif; color: var(--ink);
  }
  .stripe-band {
    position: absolute; left: 0; width: 100%;
    background: repeating-linear-gradient(90deg, var(--stripe) 0 28px, var(--paper) 28px 57px);
    background-position: 10px 0;
  }
  .stripe-band--top { top: 0; height: 66px; }
  .stripe-band--bottom { bottom: 0; height: 78px; }
  .page-title {
    position: absolute; left: 88px; top: 78px; margin: 0;
    font-weight: 300; font-size: 62px; line-height: 1; letter-spacing: -0.5px;
  }
  .page-title .ar { font-family: "Cairo", sans-serif; font-weight: 400; font-size: 52px; }
  .dish { position: absolute; width: 487px; }
  .dish__head { display: flex; align-items: center; height: 38px; }
  .dish__code {
    width: 50px; height: 38px; background: var(--label); color: #fff;
    font-weight: 500; font-size: 25px; line-height: 38px; text-align: center;
  }
  .dish__name { margin-left: 14px; font-weight: 300; font-size: 24px; flex: 1; }
  .dish__name .ar { font-family: "Cairo", sans-serif; font-size: 19px; }
  .dish__price { font-weight: 300; font-size: 24px; }
  .dish__desc {
    margin: 12px 0 0 64px; color: var(--muted); font-weight: 300; font-size: 19px; line-height: 25px;
  }
  .dish__desc-ar {
    margin: 2px 0 0 64px; width: 425px; color: var(--muted);
    font-family: "Cairo", sans-serif; font-weight: 300; font-size: 17px; line-height: 26px;
    text-align: right;
  }
  .photo {
    position: absolute; background: var(--frame); padding: 5px;
    box-shadow: 0 2px 6px rgba(0,0,0,0.3);
  }
  .photo__fill { width: 100%; height: 100%; }
  .photo__tag {
    position: absolute; left: 8px; bottom: 6px; background: var(--label); color: #fff;
    font-weight: 500; font-size: 18px; padding: 0 9px; line-height: 26px;
  }
</style>
</head>
<body>
<main class="menu-page">
  <div class="stripe-band stripe-band--top"></div>
  <div class="stripe-band stripe-band--bottom"></div>

  <h1 class="page-title">Appetizers / <span class="ar">مقبلات</span></h1>

  <figure class="photo" style="left:578px;top:22px;width:198px;height:150px;transform:rotate(-4deg);margin:0">
    <div class="photo__fill" role="img" aria-label="Grilled chicken satay skewers with peanut sauce and lime" style="background:linear-gradient(135deg,#c88a3a,#8a4a22 55%,#6f8f3a)"></div>
    <span class="photo__tag">101</span>
  </figure>
  <figure class="photo" style="left:1000px;top:36px;width:165px;height:160px;transform:rotate(-3deg);margin:0">
    <div class="photo__fill" role="img" aria-label="Crispy dendeng beef shreds on a white plate" style="background:radial-gradient(circle at 55% 45%,#8a2a1a,#5a1810 60%,#f2f0ee 90%)"></div>
    <span class="photo__tag">103</span>
  </figure>
  <figure class="photo" style="left:776px;top:38px;width:216px;height:140px;margin:0">
    <div class="photo__fill" role="img" aria-label="Grilled shrimp satay with dipping sauce" style="background:linear-gradient(120deg,#e08a3a,#c8642a 50%,#8a4a2a)"></div>
    <span class="photo__tag">102</span>
  </figure>
  <figure class="photo" style="left:614px;top:608px;width:208px;height:158px;transform:rotate(-2deg);margin:0">
    <div class="photo__fill" role="img" aria-label="Fried calamari in a white bowl with chili sauce" style="background:linear-gradient(135deg,#d8b07a,#e8cfa0 55%,#b8281a 95%)"></div>
    <span class="photo__tag">104</span>
  </figure>
  <figure class="photo" style="left:856px;top:610px;width:226px;height:148px;margin:0">
    <div class="photo__fill" role="img" aria-label="Crispy spring rolls with salad garnish" style="background:linear-gradient(135deg,#5f8a3a,#c87a2a 45%,#d89a4a 75%,#a0281a)"></div>
    <span class="photo__tag">105</span>
  </figure>

  <section class="dish" style="left:88px;top:218px">
    <div class="dish__head"><span class="dish__code">101</span><span class="dish__name">Chicken Satay / <span class="ar">ساتيه الدجاج</span></span><span class="dish__price">SR25</span></div>
    <p class="dish__desc">Lorem ipsum dolor sit amet, consectetuer adipiscing elit,<br>sed diam nonummy nibh euismod tincidunt ut laoreet.</p>
    <p class="dish__desc-ar" dir="rtl">أسياخ الدجاج شريط BQ منقع في الأعشاب التايلاندية تقدم مع صلصة الفول السوداني منعش الحلو</p>
  </section>
  <section class="dish" style="left:88px;top:390px">
    <div class="dish__head"><span class="dish__code">102</span><span class="dish__name">Shrimp Satay / <span class="ar">ساتيه الدجاج</span></span><span class="dish__price">SR30</span></div>
    <p class="dish__desc">Lorem ipsum dolor sit amet, consectetuer adipiscing elit,<br>sed diam nonummy nibh euismod tincidunt ut laoreet.</p>
    <p class="dish__desc-ar" dir="rtl">شريط BQ أسياخ الروبيان المتبل في الأعشاب التايلاندية تقدم مع صلصة الفول السوداني منعش</p>
  </section>
  <section class="dish" style="left:88px;top:567px">
    <div class="dish__head"><span class="dish__code">103</span><span class="dish__name">Dendeng / <span class="ar">دن دينغ</span></span><span class="dish__price">SR38</span></div>
    <p class="dish__desc">Lorem ipsum dolor sit amet, consectetuer adipiscing elit,<br>sed diam nonummy nibh euismod tincidunt ut laoreet.</p>
    <p class="dish__desc-ar" dir="rtl">شريط BQ أسياخ الروبيان المتبل في الأعشاب التايلاندية تقدم مع صلصة الفول السوداني منعش</p>
  </section>
  <section class="dish" style="left:600px;top:218px;width:475px">
    <div class="dish__head"><span class="dish__code">104</span><span class="dish__name">Calamari / <span class="ar">ساتيه الدجاج</span></span><span class="dish__price">SR28</span></div>
    <p class="dish__desc">Lorem ipsum dolor sit amet, consectetuer adipiscing elit,<br>sed diam nonummy nibh euismod tincidunt ut laoreet.</p>
    <p class="dish__desc-ar" dir="rtl">أسياخ الدجاج شريط BQ منقع في الأعشاب التايلاندية تقدم مع صلصة الفول السوداني منعش الحلو</p>
  </section>
  <section class="dish" style="left:600px;top:390px;width:475px">
    <div class="dish__head"><span class="dish__code">105</span><span class="dish__name">Spring Rolls / <span class="ar">ساتيه الدجاج</span></span><span class="dish__price">SR23</span></div>
    <p class="dish__desc">Lorem ipsum dolor sit amet, consectetuer adipiscing elit,<br>sed diam nonummy nibh euismod tincidunt ut laoreet.</p>
    <p class="dish__desc-ar" dir="rtl">شريط BQ أسياخ الروبيان المتبل في الأعشاب التايلاندية تقدم مع صلصة الفول السوداني منعش</p>
  </section>
</main>
</body>
</html>
```